Business Card Design Project

We need a business card to reflect the design of our website - just so it all ties in - it has a retro feel and can be found at http://www.velorasoulpair.com
We will need our phone 0437 215 964
Web address, and email velorapair@fernmail.com included
Our catch cry is "Classic Cocktail Music"
Perfect Live Music for Private & Corporate Events, Weddings and Dinner Music
Our names should be included :-
Maribel Thorne / piano & Dennis Holloway / bass
I am now also including our logo so that it can be included (in part or whole) somehow in the design
My partner thinks we should include our logo in some form in the design of the card - i will attach this here for you. I will attach eps but if you prefer another format please let me know
Regards
Mari

```html
<!DOCTYPE html>
<html lang="en">
<head>
<meta charset="utf-8">
<title>Velora Soul Pair – Business Card</title>
<link rel="stylesheet" href="https://fonts.googleapis.com/css2?family=Squada+One&family=Original+Surfer&family=Philosopher:wght@700&family=Raleway:wght@300&display=swap">
<style>
  :root {
    --page: #ffffff;
    --teal: #83b3b2;
    --orange: #d65634;
    --grey-light: #ffffff;
    --grey-dark: #acacac;
    --ink-dark: #0e3232;
    --white: #ffffff;
  }
  html, body {
    margin: 0;
    padding: 0;
    width: 1200px;
    height: 1000px;
    overflow: hidden;
    background: var(--page);
  }
  .card-canvas { display: block; width: 1200px; height: 1000px; }
  .display-type { font-family: "Squada One", "Arial Narrow", sans-serif; }
  .member-name { font-size: 50px; fill: var(--white); letter-spacing: 1px; }
  .name-joiner { font-family: "Raleway", sans-serif; font-weight: 300; font-size: 46px; fill: var(--white); }
  .member-role { font-size: 32px; fill: var(--ink-dark); }
  .web-address { font-size: 58px; fill: var(--white); }
  .contact-line { font-size: 54px; fill: var(--white); }
  .catch-cry { font-family: "Original Surfer", "Comic Sans MS", cursive; font-size: 42px; fill: var(--teal); letter-spacing: 1px; }
  .service-line { font-family: "Philosopher", Georgia, sans-serif; font-weight: 700; font-size: 34px; fill: var(--orange); }
</style>
</head>
<body>
<svg class="card-canvas" viewBox="0 0 1200 1000" xmlns="http://www.w3.org/2000/svg">
  <defs>
    <radialGradient id="silver-sheen" cx="580" cy="470" r="620" gradientUnits="userSpaceOnUse">
      <stop offset="0" stop-color="var(--grey-light)"/>
      <stop offset="0.7" stop-color="var(--grey-dark)"/>
      <stop offset="1" stop-color="var(--grey-dark)"/>
    </radialGradient>
    <path id="catch-cry-arc" d="M262 405 C 420 455, 555 590, 572 790"/>
  </defs>

  <!-- card body -->
  <rect class="lower-panel" x="21" y="375" width="1160" height="413" fill="url(#silver-sheen)"/>
  <rect class="top-band" x="21" y="152" width="1160" height="223" fill="var(--teal)"/>
  <path class="corner-sweep" d="M21 375 C 300 405, 520 560, 537 788 L21 788 Z" fill="var(--orange)"/>

  <!-- duo names -->
  <text class="display-type member-name" x="40" y="212" textLength="238" lengthAdjust="spacingAndGlyphs">Maribel Thorne</text>
  <text class="name-joiner" x="292" y="210">&amp;</text>
  <text class="display-type member-name" x="340" y="212" textLength="220" lengthAdjust="spacingAndGlyphs">Dennis Holloway</text>
  <text class="display-type member-role" x="205" y="246">piano</text>
  <text class="display-type member-role" x="500" y="244">bass</text>

  <!-- web -->
  <text class="display-type web-address" x="1160" y="376" text-anchor="end" textLength="550" lengthAdjust="spacingAndGlyphs">http://www.velorasoulpair.com</text>

  <!-- catch cry -->
  <text class="catch-cry"><textPath href="#catch-cry-arc">Classic Cocktail Music</textPath></text>

  <!-- services -->
  <g class="service-list" text-anchor="end">
    <text class="service-line" x="1140" y="480">Perfect Live Music for Private</text>
    <text class="service-line" x="1140" y="521">&amp;</text>
    <text class="service-line" x="1140" y="563">Corporate Events, Weddings</text>
    <text class="service-line" x="1140" y="604">and</text>
    <text class="service-line" x="1140" y="645">Dinner Music</text>
  </g>

  <!-- contact -->
  <text class="display-type contact-line" x="40" y="690" textLength="228" lengthAdjust="spacingAndGlyphs">0437 215 964</text>
  <text class="display-type contact-line" x="30" y="762" textLength="402" lengthAdjust="spacingAndGlyphs">velorapair@fernmail.com</text>
</svg>
</body>
</html>
```